Facebook,Twitter and Google+ Page Design for a Babysitting Online Platform

I need to launch my Social Media presence on Facebook,Twitter and Google+ and therefore need Social Media Design for the 3 platforms mentioned above. I am providing a Online Babysitting Platform that will help Mothers find babysitters for their kids. The theme is trust, community feel and mother/kid relation.
Its called Little Lantern Nook.
The blue green and orange colour is the official logo.Please see attached.
Tag Line - "Get Babysitting Help from people you trust"

Please note the Tag Line is essentially a Call to Action and therefore needs to really stand out on the cover page
Updates

Dear Designers, Please note, i do not need a logo. I am startup and would like to establish a Facebook, Twitter and Google+ Page for my startup. I therefore need cover photo for these Social Media Sites . I have provided you with the logo. I am looking for something simple and not too complicated. Heres an example of a Facebook, Twitter and Google+ page for a startup called Maple Hollow: https://www.brindlepage.example/MapleHollow https://www.quillchirp.example/MapleHollow https://circles.vorneta.example/u/0/582190347761093528817/videos Thanks in advance Regards Rul

Reason: In order to ensure the best designers who maybe busy with other projects are able to apply. I am looking for something simple so please do apply

Target Market(s)

Target Customers - Mothers/Females
Colours should signify Trust, Love,Loyalty and more for women

Industry/Entity Type

Babysitting

Requirements
Must have
• Get Babysitting Help from the People you Trust is a Call to Action and has to be on the cover page
Nice to have
• Use just one simple colour and if possible have a nice clean image of Mother and Kids to show the love, compassion,trust
Should not have
• Too Many Colours, Images , Use of the Logo provided

```html
<!DOCTYPE html>
<html lang="en">
<head>
<meta charset="utf-8">
<title>Little Lantern Nook: Cover</title>
<link rel="stylesheet" href="https://fonts.googleapis.com/css2?family=Great+Vibes&display=swap">
<style>
  :root {
    --teal: #5ccfb6;
    --lime: #a6e536;
    --orange: #f8a02a;
    --white: #ffffff;
    --mist: #eaf7f5;
    --shadow: rgba(40, 60, 60, 0.55);
  }
  html, body {
    margin: 0;
    padding: 0;
    width: 1200px;
    height: 459px;
    overflow: hidden;
    background: var(--white);
  }
  .cover {
    position: relative;
    width: 1200px;
    height: 459px;
    background: var(--white);
    overflow: hidden;
  }
  .band {
    position: absolute;
    left: 0;
    width: 100%;
  }
  .band--teal-top { top: 0; height: 16px; background: var(--teal); }
  .band--lime-top { top: 23px; height: 28px; background: var(--lime); }
  .band--lime-bottom { top: 355px; height: 26px; background: var(--lime); }
  .band--teal-thin { top: 381px; height: 6px; background: var(--teal); }
  .band--orange { top: 400px; height: 59px; background: var(--orange); }

  .stitch::after {
    content: "";
    position: absolute;
    left: 0;
    right: 0;
    border-top: 1.5px dashed rgba(255, 255, 255, 0.85);
  }
  .band--teal-top.stitch::after { top: 12px; }
  .band--lime-top.stitch::after { top: 4px; }
  .band--lime-bottom.stitch::after { bottom: 4px; }

  .pattern-field {
    position: absolute;
    left: 0;
    width: 100%;
    background: var(--mist);
  }
  .pattern-field--upper { top: 55px; height: 46px; }
  .pattern-field--lower { top: 195px; height: 160px; }

  .tagline-band {
    position: absolute;
    left: 0;
    top: 101px;
    width: 100%;
    height: 94px;
    background: var(--teal);
    display: flex;
    align-items: center;
    justify-content: center;
  }
  .tagline-band::before,
  .tagline-band::after {
    content: "";
    position: absolute;
    left: 0;
    right: 0;
    border-top: 1.5px dashed rgba(255, 255, 255, 0.85);
  }
  .tagline-band::before { top: 7px; }
  .tagline-band::after { bottom: 7px; }

  .tagline {
    margin: 0;
    font-family: "Great Vibes", cursive;
    font-weight: 400;
    font-size: 50px;
    line-height: 1;
    color: var(--white);
    letter-spacing: 0.5px;
    text-shadow: 2px 2px 2px var(--shadow);
    white-space: nowrap;
  }
</style>
</head>
<body>
  <main class="cover">
    <div class="band band--teal-top stitch"></div>
    <div class="band band--lime-top stitch"></div>
    <div class="pattern-field pattern-field--upper" role="img" aria-label="Soft pale teal scallop pattern"></div>
    <section class="tagline-band">
      <h1 class="tagline">Get Babysitting Help from people you trust</h1>
    </section>
    <div class="pattern-field pattern-field--lower" role="img" aria-label="Soft pale teal scallop pattern"></div>
    <div class="band band--lime-bottom stitch"></div>
    <div class="band band--teal-thin"></div>
    <div class="band band--orange"></div>
  </main>
</body>
</html>
```